Packaging Design for Face Mask Box

We are looking for an attractive but subtle packaging design for Face Masks (for non medical use). 50pcs per box.

The brand name should be "Kelvano". We have not yet got a logo or a text selected (font) for the brand name so we are open to your ideas on how "Kelvano" could look. It could have some elements of fresh air or breathing etc so symbolize clean and healthier air or something along those lines.

The box dimensions should be 180mm (L) x 100mm (W) x 90mm (H).

The box should have a perforation on top - exactly similar to Tissue Box packs. So, in order to access the face masks, the user should tear off the perforation and extract one mask at a time.

As this is not a medical grade face mask, the product should indicate "For Non- Medical Use". Also the heading of the masks should be DISPOSABLE PROTECTIVE FACE MASKS with sub heading 3 PLY FACE MASKS WITH EAR LOOP.

We will also prefer to have the Instructions to use and Precautions which are commonly available on face mask packages. This could be printed either on the sides or on the bottom of the package. There should also be a blank space on one of the sides to print Batch No. Mfg Date and Exp Date.

The box design could have some design resemblance to our company logo which is hereby attached in high resolution. However this is not compulsory.

The following phrases could be mentioned on the box to highlight some of the product features:

Dual Charge Electrostatic fibres for extra filtration
Improved Nose Bridge Strips for better protection
Tri-layer barrier with 3 x 25 g/m2 material
In-house production of filter material for Quality Consistency

I have added 3 samples face mask box designs from other manufacturers for your reference to get an idea of the box shape etc.

If you have any more questions, please feel free to ask.

Good luck!

```html
<!DOCTYPE html>
<html lang="en">
<head>
<meta charset="utf-8">
<title>Kelvano Face Mask Box Dieline</title>
<link href="https://fonts.googleapis.com/css2?family=Montserrat:ital,wght@0,400;0,500;0,600;1,400&display=swap" rel="stylesheet">
<style>
  :root {
    --sky-light: #4db6ec;
    --sky-mid: #0f5b85;
    --navy: #062b4d;
    --navy-deep: #041b34;
    --ice: #d6e6f0;
    --ink: #111;
    --cut: #e0193f;
    --fold: #1ab0ef;
    --brand-blue: #2a7fb8;
    --silver: linear-gradient(90deg, #bdbdbd 0%, #f4f4f4 22%, #bababa 48%, #c8c8c8 60%, #ffffff 78%, #c2c2c2 100%);
  }
  * { box-sizing: border-box; margin: 0; padding: 0; }
  html, body { width: 1099px; height: 1200px; overflow: hidden; background: #fff; }
  body { font-family: "Montserrat", sans-serif; color: var(--ink); }
  .canvas { position: relative; width: 1099px; height: 1200px; background: #fff; }

  .panel { position: absolute; overflow: hidden; }
  .flip { transform: rotate(180deg); }

  /* Front / lid panel */
  .face { width: 494px; height: 247px; }
  .face .sky { position: absolute; left: 0; top: 0; width: 100%; height: 160px;
    background: linear-gradient(180deg, var(--sky-light) 0%, #1d7fb0 40%, var(--navy) 100%); }
  .face .wave-art { position: absolute; right: 0; top: 0; width: 290px; height: 160px;
    background: radial-gradient(ellipse at 55% 75%, rgba(255,255,255,.20), rgba(255,255,255,0) 60%),
                linear-gradient(120deg, rgba(255,255,255,0) 30%, rgba(255,255,255,.10) 70%, rgba(255,255,255,0) 100%); }
  .company-mark { position: absolute; left: 0; width: 100%; top: 36px; text-align: center;
    font-size: 7px; font-weight: 500; color: #fff; letter-spacing: .02em; }
  .company-mark .dot { display: inline-block; width: 8px; height: 8px; background: #fff; margin-right: 4px; vertical-align: -1px; }
  .face .brand { position: absolute; left: 36px; top: 104px; font-size: 25px; font-weight: 600;
    color: #fff; letter-spacing: .55em; }
  .silver { position: absolute; left: 0; width: 100%; background: var(--silver); }
  .face .silver { top: 160px; height: 72px; }
  .eyebrow { font-size: 8px; letter-spacing: .36em; font-weight: 500; color: #222; }
  .title { font-weight: 500; color: var(--ink); letter-spacing: .02em; }
  .face .eyebrow { position: absolute; left: 37px; top: 16px; }
  .face .title { position: absolute; left: 36px; top: 27px; font-size: 27px; }
  .subtitle { font-style: italic; font-size: 9.5px; line-height: 10px; text-align: right; color: #222; }
  .face .subtitle { position: absolute; right: 36px; top: 30px; }
  .strip { position: absolute; left: 0; width: 100%; background: var(--navy-deep); color: #fff;
    font-size: 9px; font-weight: 500; }
  .face .strip { top: 232px; height: 15px; }
  .face .strip .non-medical { position: absolute; left: 251px; top: 2px; }
  .face .strip .count { position: absolute; right: 36px; top: 2px; }

  /* Side panel */
  .side { width: 274px; height: 247px; }
  .side .sky { position: absolute; left: 0; top: 0; width: 100%; height: 160px;
    background: linear-gradient(180deg, var(--sky-light) 0%, #1d7fb0 45%, var(--navy) 100%); }
  .side .eyebrow { position: absolute; left: 61px; top: 68px; color: #fff; font-size: 7px; letter-spacing: .3em; }
  .side .title { position: absolute; left: 60px; top: 84px; font-size: 21px; color: #fff; }
  .side .subtitle { position: absolute; right: 20px; top: 134px; color: #fff; font-size: 8px; line-height: 9px; }
  .side .silver { top: 160px; height: 74px; }
  .side .brand { position: absolute; left: 0; width: 100%; top: 24px; text-align: center;
    font-size: 20px; font-weight: 500; letter-spacing: .5em; padding-left: .5em; color: var(--ink); }
  .side .strip { top: 234px; height: 13px; font-size: 8px; }
  .side .strip .non-medical { position: absolute; left: 32px; top: 1px; }
  .side .strip .count { position: absolute; left: 189px; top: 1px; }

  /* Instructions panel */
  .guide { width: 274px; height: 247px;
    background: linear-gradient(180deg, var(--sky-light) 0%, #1b78a8 35%, var(--navy) 70%, var(--navy-deep) 100%); color: #fff; }
  .guide h2 { position: absolute; left: 0; width: 100%; top: 21px; text-align: center;
    font-size: 13px; font-weight: 500; letter-spacing: .02em; }
  .guide .lead { position: absolute; left: 0; width: 100%; top: 37px; text-align: center; font-size: 8px; }
  .step { position: absolute; top: 59px; width: 60px; }
  .step .figure { width: 60px; height: 58px; background: #f4f7fa; border-radius: 6px; }
  .step p { font-size: 5.5px; line-height: 6px; text-align: center; margin-top: 4px; }
  .guide ol { position: absolute; left: 39px; top: 152px; width: 200px; list-style: none;
    font-size: 7.2px; line-height: 8.6px; }

  /* Back panel */
  .back { left: 321px; top: 300px; width: 494px; height: 275px; background: #fff; }
  .maker { position: absolute; left: 40px; top: 204px; font-size: 9px; font-weight: 500; line-height: 12px; }
  .maker .company { color: var(--brand-blue); font-size: 10.5px; font-weight: 400; margin: 1px 0 3px; }
  .maker .company strong { color: #1c4b7a; font-weight: 600; }
  .dates { position: absolute; left: 262px; top: 200px; font-size: 8.5px; line-height: 9px; font-weight: 500; }
  .batch-box { position: absolute; left: 264px; top: 223px; width: 76px; height: 20px; border: 1px solid #222; }

  /* Bottom (dispensing) panel */
  .dispense { left: 321px; top: 822px; width: 494px; height: 275px; background: var(--ice); }
  .dispense .promo { position: absolute; left: 0; width: 100%; top: 42px; text-align: center;
    color: #fff; font-size: 23px; font-weight: 400; line-height: 28px; letter-spacing: -.01em; }
  .dispense .open { position: absolute; left: 224px; top: 131px; width: 44px; text-align: center; font-size: 9.5px; }
  .features { position: absolute; left: 20px; top: 206px; list-style: none; font-size: 8.4px; line-height: 9.8px; }
  .features li::before { content: "\2022  "; }
  .dispense .brand { position: absolute; right: 14px; top: 212px; font-size: 24px; font-weight: 500; letter-spacing: .5em; }

  .dieline { position: absolute; left: 0; top: 0; pointer-events: none; }
</style>
</head>
<body>
<div class="canvas">

  <!-- Lid / front panel -->
  <section class="panel face" style="left:321px;top:54px;">
    <div class="sky"></div>
    <div class="wave-art" role="img" aria-label="Flowing white line wave pattern"></div>
    <div class="company-mark"><span class="dot"></span>NORVEL TRADING FZC</div>
    <div class="brand">KELVANO</div>
    <div class="silver">
      <p class="eyebrow">DISPOSABLE PROTECTIVE</p>
      <h1 class="title">FACE MASK</h1>
      <p class="subtitle">3 PLY FACE MASKS<br>WITH EAR LOOP</p>
    </div>
    <div class="strip"><span class="non-medical">NON MEDICAL USE</span><span class="count">50 MASKS</span></div>
  </section>

  <!-- Back panel with batch info -->
  <section class="panel back">
    <div class="maker">
      <p>Manufactured by</p>
      <p class="company"><strong>NORVEL</strong> TRADING FZC</p>
      <p>www.kelvano.com</p>
    </div>
    <div class="dates"><p>Mfg:&nbsp; 12/06/2020</p><p>Exp:&nbsp; 12/05/2025</p></div>
    <div class="batch-box"></div>
  </section>

  <!-- Left side panel -->
  <section class="panel side flip" style="left:47px;top:575px;">
    <div class="sky"></div>
    <p class="eyebrow">DISPOSABLE PROTECTIVE</p>
    <h2 class="title">FACE MASK</h2>
    <p class="subtitle">3 PLY FACE MASKS<br>WITH EAR LOOP</p>
    <div class="silver"><div class="brand">KELVANO</div></div>
    <div class="strip"><span class="non-medical">NON MEDICAL USE</span><span class="count">50 MASKS</span></div>
  </section>

  <!-- Base / front panel (printed upside down) -->
  <section class="panel face flip" style="left:321px;top:575px;">
    <div class="sky"></div>
    <div class="wave-art" role="img" aria-label="Flowing white line wave pattern"></div>
    <div class="company-mark"><span class="dot"></span>NORVEL TRADING FZC</div>
    <div class="brand">KELVANO</div>
    <div class="silver">
      <p class="eyebrow">DISPOSABLE PROTECTIVE</p>
      <h2 class="title">FACE MASK</h2>
      <p class="subtitle">3 PLY FACE MASKS<br>WITH EAR LOOP</p>
    </div>
    <div class="strip"><span class="non-medical">NON MEDICAL USE</span><span class="count">50 MASKS</span></div>
  </section>

  <!-- Right side instructions panel -->
  <section class="panel guide flip" style="left:815px;top:575px;">
    <h2>INSTRUCTIONS</h2>
    <p class="lead">Using the correct way to wear better result</p>
    <div class="step" style="left:35px;"><div class="figure" role="img" aria-label="Illustration: hanging ear straps over both ears"></div><p>Ear straps hang<br>from both ears</p></div>
    <div class="step" style="left:106px;"><div class="figure" role="img" aria-label="Illustration: adjusting the nose bridge strip"></div><p>Adjust the twig of<br>bridge of nose</p></div>
    <div class="step" style="left:177px;"><div class="figure" role="img" aria-label="Illustration: opening the folded mask"></div><p>Open foldable part</p></div>
    <ol>
      <li>1. The mask should be replaced in time and<br>&nbsp;&nbsp;&nbsp;&nbsp;long-term use is not recommended.</li>
      <li>2. It is suggested to stop using if there is any<br>&nbsp;&nbsp;&nbsp;&nbsp;unfitness or advers reaction in the process<br>&nbsp;&nbsp;&nbsp;&nbsp;wearing.</li>
      <li>3. This product is not washable. Please ensure<br>&nbsp;&nbsp;&nbsp;&nbsp;that it is used within the validity period.</li>
      <li>4. Store in a dry, ventilated place and stay<br>&nbsp;&nbsp;&nbsp;&nbsp;away from fire and flammable materials.</li>
    </ol>
  </section>

  <!-- Top dispensing panel -->
  <section class="panel dispense">
    <p class="promo">3 PLY FACE MASKS<br>WITH EAR LOOP</p>
    <p class="open">OPEN</p>
    <ul class="features">
      <li>Dual Charge Electrostatic fibres for extra filtration</li>
      <li>Improved Nose Bridge Strips for better protection</li>
      <li>Tri-layer barrier with 3 x 25 g/m2 material</li>
      <li>In-house production of filter material for Quality Consistencyz</li>
    </ul>
    <div class="brand">KELVANO</div>
  </section>

  <!-- Cut and fold lines -->
  <svg class="dieline" width="1099" height="1200" viewBox="0 0 1099 1200" aria-hidden="true">
    <g fill="none" stroke="var(--cut)" stroke-width="1.2">
      <path d="M321 54 L299 58 L299 296 L321 300"/>
      <path d="M815 54 L837 58 L837 296 L815 300"/>
      <path d="M321 54 L815 54"/>
      <path d="M321 300 L321 575 M815 300 L815 575"/>
      <path d="M47 575 L52 553 L317 553 L321 575"/>
      <path d="M815 575 L820 553 L1085 553 L1089 575"/>
      <path d="M47 575 L47 822 M1089 575 L1089 822"/>
      <path d="M47 822 L92 981 Q95 987 102 987 L315 987 L315 830 L321 822"/>
      <path d="M1089 822 L1044 981 Q1041 987 1034 987 L821 987 L821 827 L815 822"/>
      <path d="M321 822 L321 1097 M815 822 L815 1097"/>
      <path d="M321 1097 L321 1108 L329 1108 L321 1108 C321 1138 345 1155 380 1155 L756 1155 C792 1155 815 1138 815 1108 L807 1108 L815 1108 L815 1097"/>
    </g>
    <g fill="none" stroke="var(--fold)" stroke-width="1" stroke-dasharray="4 3">
      <path d="M321 54 L321 300 M815 54 L815 300"/>
      <path d="M321 300 L815 300"/>
      <path d="M47 575 L1089 575"/>
      <path d="M47 822 L1089 822"/>
      <path d="M321 575 L321 822 M815 575 L815 822"/>
      <path d="M321 1097 L808 1097"/>
    </g>
    <path d="M388 823 L388 898 L561 984 Q568 989 575 984 L751 898 L751 823" fill="none" stroke="#333" stroke-width="1" stroke-dasharray="1 3"/>
    <path d="M562 979 L568 969 L574 979 Z" fill="#111"/>
  </svg>

</div>
</body>
</html>
```